Needing a business Card for new fire company.

Dulvan, sales fire equipment and parts. We also do tree clearing for the forest service. My logo will be attached to this. I am also looking for a design that when people see the card it stick with them and they will remember my sales team giving it to them.

```html
<!DOCTYPE html>
<html lang="en">
<head>
<meta charset="utf-8">
<title>Dulvan Business Card</title>
<link href="https://fonts.googleapis.com/css2?family=Tenor+Sans&display=swap" rel="stylesheet">
<style>
  :root {
    --backdrop: #2b2b2d;
    --card-light: #ffffff;
    --card-shade: #e4e4e4;
    --fire-red: #c0232d;
    --ink: #111111;
    --muted: #6a6a6a;
    --rule: #333333;
  }
  * { box-sizing: border-box; margin: 0; padding: 0; }
  html, body {
    width: 1200px; height: 900px; overflow: hidden;
    background: var(--backdrop);
    font-family: "Tenor Sans", sans-serif;
  }
  .stage { position: relative; width: 1200px; height: 900px; }
  .card {
    position: absolute;
    width: 560px; height: 320px;
    background: linear-gradient(200deg, var(--card-light) 30%, var(--card-shade) 100%);
    box-shadow: 0 18px 30px rgba(0,0,0,.45);
    overflow: hidden;
  }
  .card--front { left: 60px; top: 70px; }
  .card--back { left: 580px; top: 500px; }
  .card__band {
    position: absolute; left: 0; right: 0; bottom: 0;
    height: 26px; background: var(--fire-red);
  }
  .card__rule {
    position: absolute; left: 0; right: 0; bottom: 32px;
    height: 1px; background: var(--rule);
  }
  .brand {
    position: absolute;
    display: flex; align-items: center; gap: 14px;
    color: var(--ink);
    letter-spacing: 4px;
  }
  .brand__mark { width: 18px; height: 18px; background: var(--fire-red); }
  .card--front .brand { right: 60px; top: 105px; font-size: 62px; }
  .card--back .brand { left: 42px; top: 46px; font-size: 52px; }
  .contact {
    position: absolute; left: 46px; bottom: 52px;
    color: var(--muted); font-size: 15px; line-height: 1.35;
  }
  .contact__role { font-size: 15px; }
  .contact__name { color: var(--fire-red); font-size: 19px; letter-spacing: .5px; margin-bottom: 2px; }
  .contact__line { display: flex; align-items: center; gap: 8px; }
  .contact__line + .contact__line { margin-top: 3px; }
  .contact__gap { height: 10px; }
  .icon { width: 14px; height: 14px; fill: var(--fire-red); flex: none; }
  .address {
    position: absolute; left: 290px; bottom: 64px;
    display: flex; gap: 8px; color: var(--muted); font-size: 15px; line-height: 1.35;
  }
  .address .icon { margin-top: 3px; }
</style>
</head>
<body>
<main class="stage">

  <section class="card card--front" aria-label="Card front">
    <div class="brand"><span class="brand__mark"></span>DULVAN</div>
    <div class="card__rule"></div>
    <div class="card__band"></div>
  </section>

  <section class="card card--back" aria-label="Card back">
    <div class="brand"><span class="brand__mark"></span>DULVAN</div>

    <div class="contact">
      <p class="contact__role">Director</p>
      <p class="contact__name">MARA ELLISON</p>
      <p class="contact__line">
        <svg class="icon" viewBox="0 0 24 24" aria-hidden="true"><path d="M6.6 10.8a15.1 15.1 0 0 0 6.6 6.6l2.2-2.2a1 1 0 0 1 1-.25 11.4 11.4 0 0 0 3.6.57 1 1 0 0 1 1 1V20a1 1 0 0 1-1 1A17 17 0 0 1 3 4a1 1 0 0 1 1-1h3.5a1 1 0 0 1 1 1c0 1.25.2 2.45.57 3.57a1 1 0 0 1-.25 1z"/></svg>
        (00) 0000 0000
      </p>
      <div class="contact__gap"></div>
      <p class="contact__line">
        <svg class="icon" viewBox="0 0 24 24" aria-hidden="true"><circle cx="12" cy="12" r="10"/><path d="M2 12h20M12 2c3 3 3 17 0 20M12 2c-3 3-3 17 0 20" stroke="#fff" stroke-width="1.4" fill="none"/></svg>
        www.dulvan.com
      </p>
      <p class="contact__line">
        <svg class="icon" viewBox="0 0 24 24" aria-hidden="true"><path d="M2 6h20v12H2z"/><path d="M2 6l10 7 10-7" stroke="#fff" stroke-width="1.6" fill="none"/></svg>
        mara@dulvan.com
      </p>
    </div>

    <div class="address">
      <svg class="icon" viewBox="0 0 24 24" aria-hidden="true"><path d="M12 2a7 7 0 0 0-7 7c0 5 7 13 7 13s7-8 7-13a7 7 0 0 0-7-7zm0 9.5A2.5 2.5 0 1 1 12 6.5a2.5 2.5 0 0 1 0 5z"/></svg>
      <p>11 dummy city, dummy place<br>P.O Box 0000 Dummy Land</p>
    </div>

    <div class="card__rule"></div>
    <div class="card__band"></div>
  </section>

</main>
</body>
</html>
```